Financial Services Company Needs New UI/UX

Hello!

We would like to see some UI/UX ideas for our software platform. I've attached a screen capture of our current "dashboard" (or main home page, essentially). We're looking for a very simple, clean, sleek design as there are many different pages throughout the system that will all need to coordinate. You can also view our website to see the colors and general "look" we have on there. It would be ideal for the portal to coordinate with the website since that is how they access the login page. Please submit your best ideas for the dashboard and we will reach out to our favorite designer to move forward with the rest of the pages. You can find our color hex codes on our website on the "Media" page. Should you need any other supporting logos or files please send us a message and we will try to accommodate.

Thanks!

Website: www.lendmarkbuilt.example

Target Market(s)

Our clients are contractors in the construction industry and our software helps them manage material purchases for their jobs.

Industry/Entity Type

Financial Service

Font styles to use
Sans Serif

Requirements
Must have
• The same content and language as the current dashboard but an updated look.
Should not have
• Too much distraction or busy patterns, we're looking for clean and simple and user friendly. Likely a solid or subtly textured background would be best.

```html
<!DOCTYPE html>
<html lang="en">
<head>
<meta charset="utf-8">
<title>Trellbrook Supply Dashboard</title>
<link rel="stylesheet" href="https://fonts.googleapis.com/css2?family=Open+Sans:wght@400;600&family=Roboto:wght@400;500&display=swap">
<style>
:root{
  --side:#4a86c8;
  --side-active:#3c75b9;
  --top:#1c4e7b;
  --page:#f7f7f7;
  --card:#eeeeee;
  --ink:#222;
  --muted:#555;
  --amount:#666;
  --btn:#4a86c8;
  --line:#dcdcdc;
  --green:#2ea84a;
  --red:#d9453a;
  --gold:#c9a227;
}
*{box-sizing:border-box;margin:0;padding:0}
html,body{width:1200px;height:712px;overflow:hidden}
body{font-family:"Open Sans",sans-serif;background:var(--page);position:relative;color:var(--ink)}
.sidebar{position:absolute;left:0;top:0;width:230px;height:712px;background:var(--side);color:#fff;font-family:"Roboto",sans-serif}
.avatar{position:absolute;left:87px;top:18px;width:66px;height:66px;border-radius:50%;background:radial-gradient(circle at 50% 40%,#e9c9ad,#8a5a3c 70%,#3d7a3a)}
.user-name{position:absolute;top:96px;width:100%;text-align:center;font-size:17px}
.user-loc{position:absolute;top:119px;width:100%;text-align:center;font-size:11.5px;display:flex;justify-content:center;gap:5px;align-items:center}
.side-nav{position:absolute;top:157px;left:0;width:230px;list-style:none}
.side-nav li{height:47px;display:flex;align-items:center;font-size:13.5px;padding-left:26px;gap:28px}
.side-nav li.active{background:var(--side-active);border-left:4px solid #173d66;padding-left:22px;font-weight:500}
.side-nav svg{width:24px;height:24px;fill:#fff}
.side-tools{position:absolute;bottom:18px;left:24px;right:22px;display:flex;justify-content:space-between}
.side-tools svg{width:26px;height:26px;fill:#fff}
.topbar{position:absolute;left:230px;top:0;right:0;height:56px;background:var(--top);color:#dfe8f2;font-size:12.5px}
.top-nav{position:absolute;left:26px;top:0;height:56px;display:flex;align-items:center}
.top-nav span{display:flex;align-items:center;gap:7px;padding:0 22px 0 0;margin-right:22px;border-right:1px solid #3a6a95;height:16px}
.top-nav span:last-child{border:0}
.top-nav span.current{color:#fff}
.top-nav svg{width:13px;height:13px;fill:#dfe8f2}
.brand{position:absolute;right:26px;top:13px;display:flex;align-items:center;gap:8px;color:#fff;font-size:20px}
.brand i{display:block;width:28px;height:28px;border-radius:50%;background:#fff}
.page-head{position:absolute;left:257px;top:70px;right:24px;height:37px;border-bottom:1px solid #e4e4e4}
.page-head h1{font-size:17px;font-weight:600}
.legend{position:absolute;right:0;top:8px;display:flex;gap:34px;font-size:11px;color:var(--muted)}
.legend span{display:flex;align-items:center;gap:8px}
.card{position:absolute;top:138px;width:282px;height:230px;background:var(--card);box-shadow:0 1px 3px rgba(0,0,0,.25);text-align:center}
.card header{height:38px;background:#000;color:#fff;font-size:14px;font-weight:600;display:flex;align-items:center;justify-content:center;gap:8px}
.amount{font-size:27px;color:var(--amount);margin-top:22px}
.meta{font-size:13px;color:var(--muted);line-height:18.5px}
.btn{display:inline-block;height:35px;line-height:33px;padding:0 13px;font-size:13px;border:1px solid var(--btn);border-radius:3px;color:var(--btn);background:#fff}
.btn.solid{background:var(--btn);color:#fff}
.card .actions{position:absolute;bottom:15px;left:0;right:0;display:flex;justify-content:center;gap:8px}
.panel{position:absolute;top:394px;height:259px;background:var(--card);box-shadow:0 1px 3px rgba(0,0,0,.25)}
.panel header{height:39px;border-bottom:1px solid var(--line);display:flex;align-items:center;justify-content:center;gap:8px;font-size:14px}
table{border-collapse:collapse;width:100%;table-layout:fixed;font-size:11.5px;color:var(--muted)}
th{height:32px;font-weight:400;font-size:13px;color:#333;border-right:1px solid var(--line);border-bottom:1px solid var(--line)}
td{height:47px;text-align:center;border-right:1px solid var(--line);border-bottom:1px solid var(--line);line-height:16px}
th:last-child,td:last-child{border-right:0}
tr:last-child td{border-bottom:0}
.ok{color:var(--green)}
.pending{color:var(--red);display:block}
.info-dot{display:inline-block;width:13px;height:13px;border-radius:50%;background:var(--gold);color:#5a4400;font-size:9px;line-height:13px;font-weight:600;font-style:normal;text-align:center}
</style>
</head>
<body>
<aside class="sidebar">
  <div class="avatar" role="img" aria-label="User profile photo"></div>
  <div class="user-name">Mara Linh</div>
  <div class="user-loc"><svg width="10" height="12" viewBox="0 0 10 14"><path fill="#fff" d="M5 0a5 5 0 0 0-5 5c0 4 5 9 5 9s5-5 5-9a5 5 0 0 0-5-5zm0 7a2 2 0 1 1 0-4 2 2 0 0 1 0 4z"/></svg>Ho Chi Minh City, Vietnam</div>
  <ul class="side-nav">
    <li class="active"><svg viewBox="0 0 24 24"><path d="M12 2a10 10 0 1 0 0 20 10 10 0 0 0 0-20zm0 2a8 8 0 1 1 0 16 8 8 0 0 1 0-16zm-1 2h2v7h-2z"/></svg>Dashboard</li>
    <li><svg viewBox="0 0 24 24"><path d="M19 4h-1V2h-2v2H8V2H6v2H5a2 2 0 0 0-2 2v14a2 2 0 0 0 2 2h14a2 2 0 0 0 2-2V6a2 2 0 0 0-2-2zm0 16H5V9h14zM7 11h5v5H7z"/></svg>Calendar</li>
    <li><svg viewBox="0 0 24 24"><path d="M20 2H4a2 2 0 0 0-2 2v18l4-4h14a2 2 0 0 0 2-2V4a2 2 0 0 0-2-2zm-7 12h-2v-2h2zm0-4h-2V5h2z"/></svg>Announcement</li>
    <li><svg viewBox="0 0 24 24"><path d="M19 3h-4.2a3 3 0 0 0-5.6 0H5a2 2 0 0 0-2 2v15a2 2 0 0 0 2 2h14a2 2 0 0 0 2-2V5a2 2 0 0 0-2-2zm-7 0a1 1 0 1 1 0 2 1 1 0 0 1 0-2zm2 14H7v-2h7zm3-4H7v-2h10zm0-4H7V7h10z"/></svg>Courses</li>
    <li><svg viewBox="0 0 24 24"><path d="M20 4H4a2 2 0 0 0-2 2v12a2 2 0 0 0 2 2h16a2 2 0 0 0 2-2V6a2 2 0 0 0-2-2zm0 4-8 5-8-5V6l8 5 8-5z"/></svg>Messages</li>
    <li><svg viewBox="0 0 24 24"><path d="M21 6h-2v9H6v2a1 1 0 0 0 1 1h11l4 4V7a1 1 0 0 0-1-1zm-4 6V3a1 1 0 0 0-1-1H3a1 1 0 0 0-1 1v14l4-4h10a1 1 0 0 0 1-1z"/></svg>Forum</li>
  </ul>
  <div class="side-tools">
    <svg viewBox="0 0 24 24"><path d="M19.4 13a7.5 7.5 0 0 0 0-2l2.1-1.6-2-3.5-2.5 1a7 7 0 0 0-1.7-1L15 3h-4l-.4 2.9a7 7 0 0 0-1.7 1l-2.5-1-2 3.5L6.6 11a7.5 7.5 0 0 0 0 2l-2.1 1.6 2 3.5 2.5-1a7 7 0 0 0 1.7 1L11 21h4l.4-2.9a7 7 0 0 0 1.7-1l2.5 1 2-3.5zM13 15.5a3.5 3.5 0 1 1 0-7 3.5 3.5 0 0 1 0 7z"/></svg>
    <svg viewBox="0 0 24 24"><path d="M2 5h20v14H2zm2 2v.5l8 5.5 8-5.5V7l-8 5.5zm0 3V17h16v-7l-8 5.5z"/></svg>
    <svg viewBox="0 0 24 24"><path d="M6.6 10.8a15 15 0 0 0 6.6 6.6l2.2-2.2a1 1 0 0 1 1-.3 11.4 11.4 0 0 0 3.6.6 1 1 0 0 1 1 1V20a1 1 0 0 1-1 1A17 17 0 0 1 3 4a1 1 0 0 1 1-1h3.5a1 1 0 0 1 1 1 11.4 11.4 0 0 0 .6 3.6 1 1 0 0 1-.3 1z"/></svg>
    <svg viewBox="0 0 24 24"><path d="M11 2h2v10h-2zm5.6 2.4 1.4 1.4a8 8 0 1 1-12 0l1.4-1.4a6 6 0 1 0 9.2 0zM11 21h2v2h-2z"/></svg>
  </div>
</aside>

<header class="topbar">
  <nav class="top-nav">
    <span><svg viewBox="0 0 16 16"><path d="M8 1 0 8h2v7h4v-5h4v5h4V8h2z"/></svg>Home</span>
    <span class="current"><svg viewBox="0 0 16 16"><circle cx="9" cy="2" r="2"/><path d="M7 5h3l2 4h2v1h-3l-1-2-1 3 2 2v3H9v-2l-2-2-2 4H3l3-6 1-3-2 1v2H4V6z"/></svg>Job Center</span>
    <span><svg viewBox="0 0 16 16"><path d="M1 3h14v10H1zm1 2v1.5h12V5zm0 3.5V12h12V8.5z"/></svg>Payments</span>
    <span><svg viewBox="0 0 16 16"><path d="M8 1 1 4v1h14V4zM2 6h2v6H2zm5 0h2v6H7zm5 0h2v6h-2zM1 13h14v2H1z"/></svg>Credit Management</span>
    <span><svg viewBox="0 0 16 16"><path d="M4 1h8l3 3-8 11H1V9z"/></svg>Prelien Center</span>
  </nav>
  <div class="brand"><i></i>Trellbrook Supply</div>
</header>

<section class="page-head">
  <h1>Dashboard</h1>
  <div class="legend">
    <span><svg width="13" height="12" viewBox="0 0 13 12"><path fill="var(--green)" d="M6.5 0 13 12H0z"/><path fill="#fff" d="M6 4h1v4H6zm0 5h1v1H6z"/></svg>Indicates an Action is Required</span>
    <span><i class="info-dot">?</i>Information only-no action required</span>
  </div>
</section>

<article class="card" style="left:272px">
  <header><svg width="16" height="16" viewBox="0 0 16 16"><circle cx="8" cy="8" r="8" fill="#fff"/><path d="M7 7h2v5H7zm0-3h2v2H7z"/></svg>Available Master Credit</header>
  <div class="amount">$129,500.00</div>
  <p class="meta" style="margin-top:34px">Master Credit Limit: $250,000.00</p>
  <div class="actions"><span class="btn solid">Setup New Job</span></div>
</article>

<article class="card" style="left:576px">
  <header><svg width="16" height="16" viewBox="0 0 16 16"><circle cx="8" cy="8" r="8" fill="#fff"/><path d="M7 7h2v5H7zm0-3h2v2H7z"/></svg>Last Payment</header>
  <div class="amount">$500.00</div>
  <p class="meta" style="margin-top:34px">Last Payment date: 6/28/2016</p>
  <div class="actions"><span class="btn">View Payments</span><span class="btn">View Billings</span></div>
</article>

<article class="card" style="left:879px">
  <header><svg width="16" height="14" viewBox="0 0 16 14"><path fill="var(--green)" d="M8 0l8 14H0z"/><path d="M7 5h2v4H7zm0 5h2v2H7z"/></svg>Next Payment</header>
  <div class="amount">$158.95</div>
  <p class="meta" style="margin-top:14px">Due Date: 7/11/2016<br>Current Principal: $9,968.46<br>Minimum Interest/Fees: $158.9</p>
  <div class="actions"><span class="btn">Make Payment</span></div>
</article>

<section class="panel" style="left:257px;width:444px">
  <header><svg width="16" height="12" viewBox="0 0 16 12"><path fill="#222" d="M0 6h2v6H0zm3-3h2v9H3zm3 2h2v7H6zm3-5h2v12H9zm3 4h2v8h-2z"/></svg>Task Summery</header>
  <table>
    <colgroup><col style="width:37px"><col style="width:110px"><col style="width:218px"><col></colgroup>
    <tr><th></th><th>Task</th><th>Status</th><th>Received</th></tr>
    <tr><td><i class="info-dot">?</i></td><td>Supplier Invoice</td><td>Confirmation by Account Manager<span class="pending">Pending</span></td><td>5/1/2016</td></tr>
    <tr><td></td><td></td><td></td><td></td></tr>
    <tr><td></td><td></td><td></td><td></td></tr>
    <tr><td></td><td></td><td></td><td></td></tr>
  </table>
</section>

<section class="panel" style="left:716px;width:460px">
  <header><svg width="16" height="16" viewBox="0 0 16 16"><path fill="#222" d="M2 0l3 3-1 1 8 8 1-1 3 3-2 2-3-3 1-1-8-8-1 1-3-3zm9 1 4 4-3 1-2-2zM1 13l5-5 2 2-5 5z"/></svg>Active Jobs</header>
  <table>
    <colgroup><col style="width:93px"><col style="width:91px"><col style="width:91px"><col style="width:94px"><col></colgroup>
    <tr><th>Job#</th><th>Job Name</th><th>Status</th><th>Credit Limit</th><th>Avail. Credit</th></tr>
    <tr><td>pc101-001</td><td>Job #001</td><td class="ok">Active</td><td>$50,100.00</td><td>$35,100.00</td></tr>
    <tr><td>pc101-002</td><td>Job #002</td><td class="ok">Active</td><td>$40,000.00</td><td>$2,000.00</td></tr>
    <tr><td>pc101-003</td><td>Job #003</td><td class="ok">Active</td><td>$22,000.00</td><td>$0.00</td></tr>
    <tr><td>pc101-004</td><td>Job #004</td><td class="ok">Active</td><td>$10,400.00</td><td>$10,400.00</td></tr>
  </table>
</section>
</body>
</html>
```